We provide career management services supported by 6 tools designed to assist our members in managin

We have our site up and running but need to change the overall look and feel of the site, from the external pages to the internal customer facing pages. I need a site that will appeal to recent college grads as the primary target audience to customer in there 50's either trying to hold on to the job they have or trying to move on.

I would like to have 2 pages designed for this contest, the home page and the customer internal dashboard page. You can view the home page at www.jobvexara.com. I have taken two screen shots of the not completed Dashboard page, top and bottom.

The winner of this contest will be hired by us to design all remaining pages for the site including our tools.
Updates

Project Deadline Extended
Reason: We are revising the specifications for the requested designs in an attempt at better conveying what we are looking for. Most designs received so far have been a reiteration of what we currently have and realize this may be due to a lack of communication. We will have our new spec up on Tuesday.

Target Market(s)

Recent grads.

Industry/Entity Type

College

Requirements
Must have
• Overall must feel professional but have a bit of fun to it. Colors of the site should lend themselves to our logo. Please go to jobvexara.com and take a look at logo and existing pages.

```html
<!DOCTYPE html>
<html lang="en">
<head>
<meta charset="utf-8">
<title>JobVexara – Your Career is a Journey</title>
<link href="https://fonts.googleapis.com/css2?family=Open+Sans:wght@400;600;700&display=swap" rel="stylesheet">
<style>
:root{
  --ink:#222;
  --muted:#555;
  --topbar:#111;
  --red:#b3141b;
  --red-dark:#8c0d12;
  --orange:#f5a41a;
  --yellow:#f6c21c;
  --link:#b3141b;
  --social:#1f6fb3;
  --white:#fff;
}
*{box-sizing:border-box;margin:0;padding:0}
html,body{width:670px;height:1200px;overflow:hidden}
body{font-family:"Open Sans",Arial,sans-serif;color:var(--ink);background:var(--white);position:relative;font-size:10px}
.wrap{position:absolute;left:50px;right:50px}

.topbar{position:absolute;top:0;left:0;width:670px;height:34px;background:var(--topbar)}
.brand{position:absolute;left:50px;top:3px;color:var(--orange);font-weight:700;font-size:18px;line-height:22px}
.brand-tag{position:absolute;left:50px;top:24px;color:#bbb;font-size:6px;line-height:8px}
.account{position:absolute;right:50px;top:11px;color:#ddd;font-size:8px;display:flex;gap:14px}
.account span::before{content:"";display:inline-block;width:6px;height:6px;border-radius:50%;background:#999;margin-right:4px;vertical-align:middle}

.nav{position:absolute;top:34px;left:0;width:670px;height:26px;background:linear-gradient(var(--red),var(--red-dark))}
.nav ul{list-style:none;display:flex;position:absolute;left:50px;top:0;height:26px}
.nav li{color:var(--white);font-size:9px;line-height:26px;padding:0 14px;border-right:1px solid rgba(255,255,255,.25)}
.nav li.home{padding:0 10px}
.nav li.home svg{vertical-align:middle}

.hero{position:absolute;top:60px;left:0;width:670px;height:340px;background:linear-gradient(180deg,#6b7f8c 0%,#b9a676 45%,#7b6a3a 70%,#4a3d1e 100%)}
.hero-band{position:absolute;left:120px;right:120px;top:236px;height:88px;background:rgba(0,0,0,.55);text-align:center;color:var(--white);padding-top:8px}
.hero-band h1{font-weight:400;font-size:30px;line-height:1.2}
.hero-band p{font-size:19px;margin-top:2px}
.dots{position:absolute;top:404px;left:0;width:670px;text-align:center}
.dots i{display:inline-block;width:6px;height:6px;border-radius:50%;background:#ccc;margin:0 2px}
.dots i.on{background:var(--orange)}

.intro{top:424px;height:190px}
.intro-text{position:absolute;left:0;width:270px;font-size:7.5px;line-height:1.5;color:var(--muted)}
.intro-text p{margin-bottom:7px}
.intro-text b{color:var(--ink)}
.btn{display:block;text-align:center;color:var(--white);font-size:13px;font-weight:600;line-height:28px;border-radius:3px}
.btn-survey{position:absolute;left:0;top:142px;width:270px;background:var(--orange)}
.team-photo{position:absolute;left:290px;top:0;width:280px;height:160px;background:linear-gradient(180deg,#eef1f4,#c9d0d8 60%,#3a4453)}
.team-caption{position:absolute;left:300px;top:170px;font-size:11px;color:var(--ink)}

.features{top:630px;height:160px;display:flex;justify-content:space-between}
.feature{width:170px}
.feature-img{height:80px;border:1px solid #ddd}
.feature:nth-child(1) .feature-img{background:linear-gradient(135deg,#f4f4f4,#d9dde3)}
.feature:nth-child(2) .feature-img{background:linear-gradient(135deg,#d6e6f2,#7fa6c6)}
.feature:nth-child(3) .feature-img{background:linear-gradient(135deg,#e9eef2,#aab6c0)}
.feature h2{font-size:11px;font-weight:600;margin-top:8px}
.feature p{font-size:6.5px;line-height:1.45;color:var(--muted);margin-top:3px}
.feature a{font-size:6.5px;color:var(--link);text-decoration:none}

.wisdom{top:810px;height:260px}
.wisdom-text{width:290px}
.wisdom h2{font-size:13px;font-weight:400}
.wisdom .lead{font-size:8px;color:var(--muted);margin-top:6px;line-height:1.4}
.wisdom ul{list-style:none;margin-top:6px}
.wisdom li{font-size:8px;color:var(--ink);padding:3px 0;border-bottom:1px dotted #ccc}
.wisdom li::before{content:"- "}
.btn-wisdom{margin:16px 0 0 10px;width:170px;background:var(--red);font-size:12px}
.video{position:absolute;left:300px;top:14px;width:270px;height:190px;background:linear-gradient(180deg,#3d3d3d,#1a1a1a)}
.video svg.play{position:absolute;left:110px;top:68px}
.video-bar{position:absolute;left:0;right:0;bottom:0;height:14px;background:#000}
.video-bar i{position:absolute;left:8px;right:8px;top:6px;height:2px;background:#555}

.social{position:absolute;top:1110px;left:0;width:670px;height:60px;background:var(--yellow)}
.social ul{list-style:none;display:flex;justify-content:space-between;position:absolute;left:50px;right:50px;top:19px}
.social li{font-size:9px;color:var(--ink);display:flex;align-items:center;gap:6px}
.social li i{width:22px;height:22px;border-radius:50%;background:var(--social);display:inline-block}
.social li:nth-child(2) i{background:#2aa3d8}
.social li:nth-child(4) i{background:var(--red)}

.footer{position:absolute;top:1176px;left:0;width:670px;height:24px;background:var(--red-dark);color:var(--white);font-size:7px}
.footer .copy{position:absolute;left:50px;top:8px}
.footer .links{position:absolute;right:50px;top:8px}
</style>
</head>
<body>

<header class="topbar">
  <div class="brand">JobVexara</div>
  <div class="brand-tag">because your career demands attention</div>
  <div class="account"><span>LOGIN</span><span>SIGNUP</span></div>
</header>

<nav class="nav">
  <ul>
    <li class="home"><svg width="12" height="11" viewBox="0 0 12 11"><path d="M6 0 0 5h2v6h3V7h2v4h3V5h2z" fill="#fff"/></svg></li>
    <li>About Job Vexara</li>
    <li>Our Team</li>
    <li>Products &amp; Services</li>
    <li>Contact</li>
  </ul>
</nav>

<section class="hero" role="img" aria-label="Photo of a long country road stretching toward the horizon at sunset">
  <div class="hero-band">
    <h1>Your Career is a Journey</h1>
    <p>are you sure you have the right guide?</p>
  </div>
</section>
<div class="dots"><i></i><i class="on"></i><i></i><i></i></div>

<section class="wrap intro">
  <div class="intro-text">
    <p><b>FINALLY!</b> Expert advice and all the tools you need to succeed are available at your fingertips!</p>
    <p><b>JobVexara</b> is a unique online career management tool and consulting service designed to meet the needs of someone like you. Be more effective getting and acing interviews. Land your dream job. Maintain success in your chosen profession. It's all possible when you have the right tools and guidance.</p>
    <p>Experience our unique, no-nonsense approach to unlocking the secrets to success that no one else will tell you. We will ease your career anxieties and help you make better career decisions.</p>
    <p>Welcome to <b>JobVexara!</b>… because your career demands attention.</p>
  </div>
  <a class="btn btn-survey">TAKE OUR SURVEY!</a>
  <div class="team-photo" role="img" aria-label="Photo of a smiling business team giving thumbs up"></div>
  <div class="team-caption">JobVexara! can give you the tools to success</div>
</section>

<section class="wrap features">
  <article class="feature">
    <div class="feature-img" role="img" aria-label="Illustration of a colorful network of connected people"></div>
    <h2>Network for Success</h2>
    <p>Navigating the job search process is tough, especially if you're doing it alone. Connect with others who can open new doors.</p>
    <a>» Read More</a>
  </article>
  <article class="feature">
    <div class="feature-img" role="img" aria-label="Photo of a motivated businessman at his desk"></div>
    <h2>Get Focused, Get Motivated</h2>
    <p>Have you made as overwhelming job search seem easier? It is possible not to miss a day, stay on track and keep going.</p>
    <a>» Read More</a>
  </article>
  <article class="feature">
    <div class="feature-img" role="img" aria-label="Photo of a job interview handshake"></div>
    <h2>Ace Your Interviews</h2>
    <p>The biggest mistake most people make? Answering questions for the first time at the interview. Practice before it counts.</p>
    <a>» Read More</a>
  </article>
</section>

<section class="wrap wisdom">
  <div class="wisdom-text">
    <h2>Take a sneak peak at our vexaraWISDOM</h2>
    <p class="lead">Our inside experts share their wisdom and best practices to ensure that our members are successful in their career journey.<br>Have you wondered about:</p>
    <ul>
      <li>What steps should an employee take to manage their own career?</li>
      <li>What things do you look for in a resume?</li>
      <li>How important are soft skills versus technical skills?</li>
      <li>What a new employee should expect from the first 30 days of a job?</li>
      <li>What characteristics do successful people have?</li>
      <li>Examples of human capital initiative</li>
    </ul>
    <a class="btn btn-wisdom">TAKE OUR SURVEY!</a>
  </div>
  <div class="video" role="img" aria-label="Video player with an introductory video">
    <svg class="play" width="50" height="50" viewBox="0 0 50 50"><circle cx="25" cy="25" r="24" fill="rgba(255,255,255,.25)"/><path d="M19 14v22l18-11z" fill="#fff"/></svg>
    <div class="video-bar"><i></i></div>
  </div>
</section>

<section class="social">
  <ul>
    <li><i></i>Join us on Friendsquare</li>
    <li><i></i>Follow us on Chirpline</li>
    <li><i></i>Join us on Linkworks</li>
    <li><i></i>Watch our Videos on Viewtube</li>
  </ul>
</section>

<footer class="footer">
  <span class="copy">Contents Copyright © 2010-2013 JobVexara</span>
  <span class="links">Home | About Job Vexara | Our Team | Products &amp; Services | Contact Us</span>
</footer>

</body>
</html>
```